Beauty Therapy Web Design

I need a web page design for a small beauty therapy clinic, the owner is currently the only beauty therapist working there.
We require the following pages:
Home
About
Treatments
Nails
Courses
Contact
I will attach the clinics business card, treatment menu and signage so that you get a feeling for the branding colours etc.
This is the first website for the beauty therapist, she would like to attract new clients and also tourists that come in on the cruise ships. The thing that sets her apart from other clinics is that she welcomes texting for appointments.
I have selected refundable because I have never done this before so I don't know what to expect, I have the full intention of going through with it as long as I get a good design.
Feel free to ask for further information
Reason: Project extended as I am away for work and am unable to meet with the owner.
Target Market(s)
Females 18 to 50
Industry/Entity Type
Business
Look and feel
Each slider illustrates characteristics of the customer's brand and the style your logo design should communicate.

```html
<!DOCTYPE html>
<html lang="en">
<head>
<meta charset="utf-8">
<title>Velora Beauty Therapy</title>
<link rel="stylesheet" href="https://fonts.googleapis.com/css2?family=Arimo:ital,wght@0,400;0,700;1,400&family=Lobster+Two:ital,wght@1,400&display=swap">
<style>
  :root {
    --violet: #5e2389;
    --orange: #e0892b;
    --orange-deep: #c9721c;
    --orange-light: #eb9a3c;
    --charcoal: #1b1b1b;
    --footer-black: #171412;
    --nav-cream: #f7e7b4;
    --rule: rgba(120, 70, 20, 0.55);
    --rule-light: rgba(255, 215, 150, 0.45);
    --white: #ffffff;
    --body-grey: #d6d6d6;
    --photo-lilac: #9b6fd6;
    --photo-deep: #6a3fae;
  }
  * { margin: 0; padding: 0; box-sizing: border-box; }
  html, body { width: 1200px; height: 894px; overflow: hidden; }
  body {
    position: relative;
    background: var(--violet);
    font-family: "Arimo", Arial, sans-serif;
    color: var(--white);
  }
  .brand { position: absolute; left: 116px; top: 18px; width: 350px; }
  .brand-name {
    font-weight: 700; font-size: 78px; line-height: 86px; letter-spacing: 1px;
    color: var(--white);
  }
  .brand-tagline {
    position: absolute; left: 122px; top: 84px;
    font-style: italic; font-size: 20px; color: var(--white);
  }
  .contact-block { position: absolute; left: 825px; top: 42px; }
  .contact-phone {
    display: flex; align-items: center; gap: 4px;
    font-weight: 700; font-size: 34px; line-height: 40px;
  }
  .contact-phone svg { width: 30px; height: 30px; }
  .contact-address { font-weight: 700; font-size: 16.5px; line-height: 22px; margin-top: 4px; }

  .showcase { position: absolute; left: 47px; top: 149px; width: 1106px; height: 593px; display: flex; }
  .nav-column {
    width: 368px; height: 100%;
    background: radial-gradient(ellipse at 40% 40%, var(--orange-light), var(--orange) 55%, var(--orange-deep));
  }
  .main-nav { list-style: none; padding-top: 48px; }
  .main-nav li { width: 236px; margin-left: 18px; border-bottom: 1px solid var(--rule); box-shadow: 0 1px 0 var(--rule-light); }
  .main-nav a {
    display: block; padding-left: 53px; height: 49.5px; line-height: 44px;
    font-style: italic; font-size: 21px; color: var(--nav-cream); text-decoration: none;
    text-shadow: 1px 2px 3px rgba(60, 25, 0, 0.75);
  }
  .feature-photo {
    width: 370px; height: 100%;
    background: radial-gradient(ellipse at 50% 35%, #d9c6e6 0%, var(--photo-lilac) 45%, var(--photo-deep) 100%);
  }
  .feature-text { width: 368px; height: 100%; background: var(--charcoal); padding: 42px 40px 0 41px; }
  .feature-title { font-family: "Lobster Two", cursive; font-style: italic; font-weight: 400; font-size: 29px; line-height: 34px; color: #f2f2f2; }
  .feature-kicker { font-size: 13px; line-height: 18px; margin-top: 5px; text-transform: uppercase; color: #e6e6e6; letter-spacing: 0.2px; }
  .feature-body p { font-size: 16px; line-height: 28.2px; color: var(--body-grey); margin-top: 38px; letter-spacing: 0.2px; }
  .feature-body p + p { margin-top: 28px; }
  .read-more { display: inline-block; margin-top: 34px; font-weight: 700; font-size: 15.5px; color: var(--white); text-decoration: none; }

  .site-footer {
    position: absolute; left: 46px; top: 778px; width: 1106px; height: 94px;
    background: var(--footer-black); text-align: center;
    padding-top: 12px; font-size: 15px; line-height: 22.5px; color: #eeeeee;
  }
  .site-footer span + span { margin-left: 12px; }
</style>
</head>
<body>
  <header>
    <div class="brand">
      <div class="brand-name">Velora</div>
      <div class="brand-tagline">Beauty Therapy</div>
    </div>
    <div class="contact-block">
      <div class="contact-phone">
        <svg viewBox="0 0 30 30" aria-hidden="true"><path d="M9 26 C4 20 4 10 11 5 L15 9 C11 12 10 17 13 21 Z M20 4 C24 3 27 5 27 7 L23 10 C22 8 20 8 18 8 Z" fill="#ffffff"/></svg>
        <span>021 555 0147</span>
      </div>
      <div class="contact-address">Cnr Kowhai St. &amp; Harbour Rd<br>Mount Kerrin</div>
    </div>
  </header>

  <main class="showcase">
    <nav class="nav-column">
      <ul class="main-nav">
        <li><a href="#">Home</a></li>
        <li><a href="#">About</a></li>
        <li><a href="#">Treatments</a></li>
        <li><a href="#">Nails</a></li>
        <li><a href="#">Courses</a></li>
        <li><a href="#">Contact</a></li>
      </ul>
    </nav>
    <div class="feature-photo" role="img" aria-label="Portrait of a model with lilac glitter eye make-up, wrapped in violet chiffon"></div>
    <section class="feature-text">
      <h1 class="feature-title">Spa Deluxe Manicure</h1>
      <div class="feature-kicker">Aliquip aperiri constituam his ea</div>
      <div class="feature-body">
        <p>No quis atomorum has. Mel in duis omnes ornatus. Posse animal definiebas ei usu, at errem omnium has. Simul mollis mel ne, in mel facete percipitur deterruisset. Zril aperiam recusabo mel et, elit reque movet eu sed.</p>
        <p>Cu brute virtute qui, exerci vidisse no has. An latine appareat inimicus his. Tollit partem eam ne. Eu senserit hendrerit aliquando mei, nec novum maiorum similique at. Vim ex saepe</p>
      </div>
      <a class="read-more" href="#">Read more</a>
    </section>
  </main>

  <footer class="site-footer">
    <div>Copyright 2012 Velora Beauty Therapy</div>
    <div><span>Phone Maree 07 555 0182</span><span>Cellphone 021 555 0147</span></div>
    <div>Cnr Kowhai St. &amp; Harbour Rd, Mount Kerrin</div>
  </footer>
</body>
</html>
```